Dorsey K. Whitfield Business Card

We need a business card for our company Dorsey K. Whitfield Heating & Plumbing to be distributed to potential customers. It should follow the color scheme of our logo and have a modern upscale and masculine look.

The logo is attached and the info below should also be included:

5187 W. Quarry Bend Rd.
Carrow Falls, PA 17652

Tobias R. Whitfield
(717) 593-8126
tobiasreedwhitfield@mailvane.com
dorseykwhitfield.com
PA #038419

Industry/Entity Type

Business

Contact Information for Business Card

5187 W. Quarry Bend Rd.
Carrow Falls, PA 17652

Tobias R. Whitfield
(717) 593-8126
tobiasreedwhitfield@mailvane.com
dorseykwhitfield.com
PA #038419

Colors

Designer to choose colors to be used in the design.

Requirements
Must have
• Information above included

```html
<!DOCTYPE html>
<html lang="en">
<head>
<meta charset="utf-8">
<title>Dorsey K. Whitfield Heating &amp; Plumbing – Business Card</title>
<link rel="stylesheet" href="https://fonts.googleapis.com/css2?family=Exo+2:wght@400;500;600&display=swap">
<style>
  :root {
    --stage: #2b2b2b;
    --card: #1e1f21;
    --blue: #0b5bb5;
    --green: #a8cf38;
    --white: #f2f2f2;
  }
  * { box-sizing: border-box; margin: 0; padding: 0; }
  html, body { width: 1200px; height: 930px; overflow: hidden; }
  body {
    background: var(--stage);
    font-family: "Exo 2", Arial, sans-serif;
    position: relative;
  }
  .card {
    position: absolute;
    width: 600px;
    height: 343px;
    background: var(--card);
    border-radius: 16px;
    overflow: hidden;
    box-shadow: 0 14px 30px rgba(0,0,0,.45);
  }

  /* Back of card */
  .card-back { left: 110px; top: 70px; }
  .brand {
    position: absolute;
    left: 150px; top: 118px;
    display: flex; align-items: center; gap: 16px;
  }
  .brand-square {
    width: 48px; height: 48px;
    background: var(--white);
  }
  .brand-name {
    color: var(--white);
    font-weight: 600;
    font-size: 22px;
    line-height: 1.15;
    text-transform: uppercase;
    letter-spacing: .5px;
  }
  .back-web {
    position: absolute;
    left: 0; right: 0; top: 278px;
    text-align: center;
    color: var(--white);
    font-size: 15px;
    letter-spacing: 1px;
  }
  .accent { color: var(--green); }

  /* Front of card */
  .card-front { left: 490px; top: 500px; }
  .person {
    position: absolute; left: 40px; top: 112px;
    font-size: 22px; font-weight: 500;
    text-transform: uppercase; letter-spacing: 1px;
    white-space: nowrap;
  }
  .person .first { color: var(--blue); }
  .person .last { color: var(--green); }
  .role {
    position: absolute; left: 42px; top: 142px;
    color: var(--white); font-size: 13px; letter-spacing: 1px;
  }
  .address {
    position: absolute; left: 42px; top: 192px;
    color: var(--white); font-size: 14px; line-height: 1.4;
  }
  .contacts {
    position: absolute; left: 42px; top: 250px;
    list-style: none;
    color: var(--white); font-size: 14px; line-height: 1.45;
  }
  .contacts li { display: flex; align-items: center; gap: 10px; white-space: nowrap; }
  .contacts svg { width: 12px; height: 12px; fill: var(--blue); flex: none; }
  .feature-square {
    position: absolute; left: 330px; top: 40px;
    width: 200px; height: 200px;
    background: var(--blue);
  }
  .bands {
    position: absolute; left: 0; top: 0; width: 600px; height: 343px;
  }
  .license-text {
    position: absolute; right: 26px; top: 264px;
    color: var(--white); font-size: 14px; letter-spacing: 1px;
  }
</style>
</head>
<body>

<section class="card card-back" aria-label="Card back">
  <div class="brand">
    <div class="brand-square"></div>
    <div class="brand-name">Dorsey K. Whitfield<br>Heating &amp; Plumbing</div>
  </div>
  <p class="back-web">www.<span class="accent">dorseykwhitfield</span>.com</p>
</section>

<section class="card card-front" aria-label="Card front">
  <div class="feature-square"></div>
  <svg class="bands" viewBox="0 0 600 343" aria-hidden="true">
    <polygon points="0,331 380,331 395,316 395,258 600,258 600,343 0,343" fill="var(--blue)"/>
    <polygon points="405,252 600,252 600,300 405,300" fill="var(--green)"/>
  </svg>
  <p class="license-text">PA #038419</p>

  <h1 class="person"><span class="first">Tobias R.</span> <span class="last">Whitfield</span></h1>
  <p class="role">PRESIDENT</p>
  <p class="address">5187 W. Quarry Bend Rd.<br>Carrow Falls, PA 17652</p>
  <ul class="contacts">
    <li>
      <svg viewBox="0 0 12 12"><rect x="3" y="0" width="6" height="12" rx="1.2"/><rect x="4.2" y="1.5" width="3.6" height="7.5" fill="var(--card)"/></svg>
      <span>(717) 593-8126</span>
    </li>
    <li>
      <svg viewBox="0 0 12 12"><rect x="0" y="2" width="12" height="8" rx="1"/><polyline points="0.5,2.5 6,7 11.5,2.5" fill="none" stroke="var(--card)" stroke-width="1.2"/></svg>
      <span>tobiasreedwhitfield@mailvane.com</span>
    </li>
    <li>
      <svg viewBox="0 0 12 12"><circle cx="6" cy="6" r="6"/><ellipse cx="6" cy="6" rx="2.4" ry="5.6" fill="none" stroke="var(--card)" stroke-width="1"/><line x1="0.5" y1="6" x2="11.5" y2="6" stroke="var(--card)" stroke-width="1"/></svg>
      <span>www.<span class="accent">dorseykwhitfield</span>.com</span>
    </li>
  </ul>
</section>

</body>
</html>
```